Dorian Felsgrove breaking. Or D. Felsgrove breaking

I break in and train horses, any age any bread of horse, for any disaplin. I need a business card that is simple but effective, in the way of looking professional. I would like a horse on my card, preferably a horse without a rider. I also pre train horse, younge horses that need a bit of riding before they go into serious work, and prepare yearlings for sale.

Reason: This is for my boyfriend, and I really want it to be perfect and impressive!

Target Market(s)

Thoroughbred race horse trainers, horse industrie people.

Industry/Entity Type

Business

Contact Information for Business Card

Dorian Felsgrove horse breaking, "WOLBUNDA" Tarrowby, give your horse the right start to any career. dfels@quillmail.com.au, 0431862097. Horse breaking~pre-training~sale preparation

```html
<!DOCTYPE html>
<html lang="en">
<head>
<meta charset="utf-8">
<title>Dorian Felsgrove – Horse Breaking Business Card</title>
<link rel="stylesheet" href="https://fonts.googleapis.com/css2?family=Handlee&family=Lato:wght@400&display=swap">
<style>
  :root {
    --card-taupe: #978574;
    --band-dark: #7b6c5d;
    --strip-dark: #6c5e50;
    --ink-light: #ffffff;
    --horse-light: #eef0f4;
    --horse-shade: #8f97a8;
  }
  * { margin: 0; padding: 0; box-sizing: border-box; }
  html, body {
    width: 1200px;
    height: 750px;
    overflow: hidden;
    background: var(--card-taupe);
  }
  .card {
    position: relative;
    width: 1200px;
    height: 750px;
    background: var(--card-taupe);
    color: var(--ink-light);
    font-family: "Lato", Arial, sans-serif;
  }
  .tagline {
    position: absolute;
    left: 56px;
    top: 60px;
    font-family: "Handlee", cursive;
    font-size: 40px;
    line-height: 70px;
    letter-spacing: 1px;
  }
  .name-band {
    position: absolute;
    left: 0;
    top: 254px;
    width: 700px;
    height: 140px;
    background: linear-gradient(90deg, var(--band-dark) 0%, var(--band-dark) 75%, rgba(123,108,93,0) 100%);
    padding: 22px 0 0 54px;
  }
  .owner-name {
    font-size: 46px;
    font-weight: 400;
    letter-spacing: 0.5px;
    line-height: 58px;
  }
  .owner-role {
    font-size: 34px;
    line-height: 44px;
  }
  .horse-art {
    position: absolute;
    left: 600px;
    top: 40px;
    width: 560px;
    height: 460px;
    border-radius: 46% 40% 38% 44%;
    background: radial-gradient(ellipse at 45% 45%, var(--horse-light) 0%, #d6dae2 45%, var(--horse-shade) 75%, rgba(143,151,168,0) 100%);
  }
  .services-strip {
    position: absolute;
    left: 0;
    top: 508px;
    width: 100%;
    height: 58px;
    background: var(--strip-dark);
    padding-left: 48px;
    font-family: "Handlee", cursive;
    font-size: 38px;
    line-height: 58px;
    letter-spacing: 1px;
  }
  .contact {
    position: absolute;
    left: 0;
    top: 604px;
    width: 100%;
    text-align: center;
    font-size: 34px;
    line-height: 52px;
  }
</style>
</head>
<body>
  <div class="card">
    <p class="tagline">give your horse the<br>right start to any career</p>

    <div class="name-band">
      <h1 class="owner-name">Dorian Felsgrove</h1>
      <p class="owner-role">Horse breaking</p>
    </div>

    <div class="horse-art" role="img" aria-label="Illustration of a grey horse trotting without a rider"></div>

    <p class="services-strip">Horse breaking - Pre-training - Sale preparation</p>

    <div class="contact">
      <p class="address">"WOLBUNDA" Tarrowby,</p>
      <p class="details">E : dfels@quillmail.com.au , T : 0431862097</p>
    </div>
  </div>
</body>
</html>
```